依頼詳細
内覧会の予定日と移転開院日のお知らせチラシを作成していただきたいです。
記載項目
表面
・病院ロゴ
・病院名:くるみ台動物病院
・内覧会開催日時:4月1日、2日 10:00~16:00
・移転開院日:4月4日(月)
・住所:愛知県知立市栄花台5-27
・病院地図
・電話番号:0566-47-3958
・病院HP URL:https://kurumidai-ah.jp
・診療時間 月〜金曜 8:30~11:30 14:00~17:00
土曜日 8:30~11:30 14:00~18:00
日曜・祝日 休診
サイズ
A4
ページ数
片面
希望イメージ
シンプル 複雑
単色 カラフル
暗い 明るい
日常 高級
遊び心 厳粛
未来的 伝統的
女性的 男性的
希望する色
赤系、茶系、緑系、黄・オレンジ系
納品ファイル
• 高解像度JPG (.jpg)
• イラストレーター形式 (.ai)
• PNG形式 (.png)
補足説明
印刷はセルモアを利用する予定です。
移転先の場所を記載した画像を追加しました。

当院の移転時期が4月ということで春らしい桜を入れていただいた点と箱の上に犬と猫が乗っているというデザインの可愛らしさからこちらのご提案に決めさせていただきました。

みなさま、素敵なご提案をいただき、誠にありがとうございました。
どれも魅力的なご提案で最後まで選出に悩みました。今後もコンペをお願いする機会があるかと思いますが、何卒よろしくお願いいたします。

```html
<!DOCTYPE html>
<html lang="ja">
<head>
<meta charset="utf-8">
<title>くるみ台動物病院 移転オープンのお知らせ</title>
<link href="https://fonts.googleapis.com/css2?family=M+PLUS+Rounded+1c:wght@500;700;800;900&display=swap" rel="stylesheet">
<style>
  :root {
    --green: #3f9a3a;
    --green-dark: #2d7a2b;
    --hill-light: #d5ea9a;
    --hill-mid: #bcdc73;
    --orange: #ef8a1c;
    --red: #d9352a;
    --blue: #3a7fc4;
    --ink: #3a2a1e;
    --cream: #fffaf0;
    --sky: #eef7fb;
    --white: #ffffff;
    --placeholder-map: #eef0ea;
  }
  * { margin: 0; padding: 0; box-sizing: border-box; }
  html, body { width: 844px; height: 1200px; overflow: hidden; background: var(--white); }
  body { font-family: "M PLUS Rounded 1c", sans-serif; color: var(--ink); }
  .flyer { position: relative; width: 844px; height: 1200px; overflow: hidden; background: linear-gradient(var(--sky), var(--cream) 60%); }

  .people-band { position: absolute; left: 0; top: 0; width: 844px; height: 300px;
    background: radial-gradient(ellipse at 20% 40%, #f7c9a0 0 18%, transparent 40%),
                radial-gradient(ellipse at 82% 45%, #c9dfb0 0 18%, transparent 40%),
                linear-gradient(#f6efe3, #fbf6ec); opacity: .85; }

  .brand { position: absolute; top: 40px; left: 0; width: 100%; text-align: center; }
  .brand-mark { display: block; width: 120px; height: 120px; margin: 0 auto 18px; border-radius: 50%; background: var(--green); }
  .brand-name { font-size: 56px; font-weight: 800; color: var(--green); letter-spacing: 2px; line-height: 1.1; }
  .brand-en { font-size: 20px; font-weight: 700; color: var(--green); margin-top: 4px; letter-spacing: 1px; }

  .headline { position: absolute; top: 370px; left: 0; width: 100%; text-align: center;
    font-size: 112px; font-weight: 900; color: var(--orange); letter-spacing: 2px; line-height: 1; }

  .open-date { position: absolute; top: 495px; right: 48px; padding: 6px 28px 8px; border-radius: 40px;
    background: var(--green); color: var(--white); font-size: 52px; font-weight: 900; line-height: 1; }
  .open-date small { font-size: 28px; }

  .hills { position: absolute; left: 0; top: 540px; width: 844px; height: 500px; }

  .preview { position: absolute; top: 585px; left: 0; width: 100%; text-align: center; }
  .preview-label { font-size: 28px; font-weight: 800; color: var(--ink); letter-spacing: 2px; line-height: 1.2; }
  .preview-dates { font-size: 88px; font-weight: 900; color: var(--ink); line-height: 1; display: flex; justify-content: center; align-items: center; gap: 8px; margin-top: 2px; }
  .day-badge { display: inline-flex; align-items: center; justify-content: center; width: 44px; height: 44px; border-radius: 50%;
    background: var(--orange); color: var(--white); font-size: 26px; font-weight: 800; line-height: 1; }
  .day-badge.sat { background: var(--blue); }
  .preview-time { font-size: 32px; font-weight: 800; color: var(--ink); letter-spacing: 1px; line-height: 1.2; margin-top: 4px; }

  .dog-art { position: absolute; left: 150px; top: 600px; width: 150px; height: 150px; border-radius: 40% 40% 20% 20%; background: #d9a66b; opacity: .8; }
  .cat-art { position: absolute; right: 160px; top: 620px; width: 120px; height: 130px; border-radius: 40% 40% 20% 20%; background: #b9b6b0; opacity: .8; }

  .map { position: absolute; left: 56px; top: 778px; width: 720px; height: 205px; border-radius: 6px; background: var(--placeholder-map); border: 2px solid #cfd6c6; }
  .address { position: absolute; left: 220px; top: 970px; padding: 6px 22px; border-radius: 24px; background: var(--red); color: var(--white); font-size: 22px; font-weight: 800; line-height: 1.3; }

  .footer { position: absolute; left: 0; top: 1040px; width: 100%; height: 160px; background: var(--white); display: flex; justify-content: space-between; align-items: center; padding: 0 48px; }
  .hours-title { display: inline-block; padding: 2px 14px; background: var(--green); color: var(--white); font-size: 16px; font-weight: 800; border-radius: 4px; margin-bottom: 6px; }
  .hours table { border-collapse: collapse; font-size: 16px; font-weight: 700; }
  .hours td { padding: 2px 10px 2px 0; }
  .contact { text-align: right; }
  .contact-name { font-size: 40px; font-weight: 800; color: var(--green); line-height: 1.1; }
  .contact-tel { font-size: 40px; font-weight: 900; color: var(--ink); display: flex; align-items: center; gap: 8px; justify-content: flex-end; line-height: 1.2; }
  .contact-url { font-size: 14px; font-weight: 700; }
</style>
</head>
<body>
<main class="flyer">
  <div class="people-band" role="img" aria-label="動物を抱いた人々のイラスト"></div>

  <header class="brand">
    <span class="brand-mark"></span>
    <h1 class="brand-name">くるみ台動物病院</h1>
    <p class="brand-en">Kurumidai Animal Hospital</p>
  </header>

  <svg class="hills" viewBox="0 0 844 500" aria-hidden="true">
    <path d="M0 120 Q220 20 440 90 T844 60 V500 H0Z" fill="var(--hill-light)"/>
    <path d="M0 260 Q300 180 600 240 T844 220 V500 H0Z" fill="var(--hill-mid)"/>
  </svg>

  <h2 class="headline">移転オープン</h2>
  <p class="open-date">4.4<small>(月)</small></p>

  <div class="dog-art" role="img" aria-label="箱の上の犬のイラスト"></div>
  <div class="cat-art" role="img" aria-label="箱の上の猫のイラスト"></div>

  <section class="preview">
    <p class="preview-label">内覧会開催</p>
    <p class="preview-dates">4.1<span class="day-badge">金</span>2<span class="day-badge sat">土</span></p>
    <p class="preview-time">10:00〜16:00</p>
  </section>

  <div class="map" role="img" aria-label="移転先周辺の地図"></div>
  <p class="address">愛知県知立市栄花台5-27</p>

  <footer class="footer">
    <div class="hours">
      <span class="hours-title">診療時間</span>
      <table>
        <tr><td>月〜金曜</td><td>8:30〜11:30</td><td>14:00〜17:00</td></tr>
        <tr><td>土曜日</td><td>8:30〜11:30</td><td>14:00〜18:00</td></tr>
        <tr><td>日曜・祝日</td><td>休診</td><td></td></tr>
      </table>
    </div>
    <div class="contact">
      <p class="contact-name">くるみ台動物病院</p>
      <p class="contact-tel">
        <svg width="36" height="36" viewBox="0 0 24 24" aria-hidden="true"><path fill="var(--ink)" d="M6.6 10.8a15 15 0 006.6 6.6l2.2-2.2a1 1 0 011-.25 11.4 11.4 0 003.6.57 1 1 0 011 1V20a1 1 0 01-1 1A17 17 0 013 4a1 1 0 011-1h3.5a1 1 0 011 1c0 1.250.2 2.45.57 3.57a1 1 0 01-.25 1z"/></svg>
        0566-47-3958
      </p>
      <p class="contact-url">https://kurumidai-ah.jp</p>
    </div>
  </footer>
</main>
</body>
</html>
```